Business Cards

The name of our firm is "Bayfield Insurance adjusters"
We separate ourselves from all other public adjusters because most of us worked for the insurance companies so we understand their games.
As Insurance adjusters we represent the Insured, not the insurance companies. Our # 1 priority is to handle the entire claim process as seamless as possible on behalf of the homeowner/business owner so they don't have to deal with the hassles and headaches. Just as the logo your team designed, I want the cards to stand out from everyone elses. I also want the cards to help better understand our services and Value on hiring us and value that we can offer.
I uploaded the logo whenever I created the project. I don't see an option on re uploading the logo anywhere. Any advise??

```html
<!DOCTYPE html>
<html lang="en">
<head>
<meta charset="utf-8">
<title>Bayfield Insurance Adjusters — Business Cards</title>
<link rel="stylesheet" href="https://fonts.googleapis.com/css2?family=Montserrat:wght@400;500;800&display=swap">
<style>
  :root {
    --backdrop: #eeeeef;
    --card: #fbfbfc;
    --brand-blue: #1763a6;
    --brand-blue-deep: #17477f;
    --ink-black: #1b1b1c;
    --ink-charcoal: #2e2e30;
    --navy-text: #141c4f;
    --shadow-grey: #c7c9d1;
  }
  * { box-sizing: border-box; margin: 0; padding: 0; }
  html, body { width: 1200px; height: 933px; overflow: hidden; }
  body {
    background: var(--backdrop);
    font-family: "Montserrat", Arial, sans-serif;
    position: relative;
  }
  .card {
    position: absolute;
    width: 520px;
    height: 297px;
    background: var(--card);
    overflow: hidden;
    box-shadow: 0 10px 24px rgba(0,0,0,0.12), 0 2px 4px rgba(0,0,0,0.08);
  }
  .card--front { left: 50px; top: 318px; }
  .card--back  { left: 630px; top: 318px; }

  .card__bands { position: absolute; inset: 0; width: 100%; height: 100%; }

  .brand {
    position: absolute;
    left: 50%;
    top: 50%;
    transform: translate(-50%, -50%);
    display: flex;
    align-items: center;
    gap: 12px;
    white-space: nowrap;
  }
  .brand__dot {
    width: 22px; height: 22px;
    border-radius: 50%;
    background: var(--brand-blue);
  }
  .brand__name {
    font-weight: 800;
    font-size: 21px;
    letter-spacing: 0.04em;
    text-transform: uppercase;
    color: var(--brand-blue-deep);
  }

  .band {
    position: absolute;
    left: 0; right: 0;
    height: 14px;
    background: linear-gradient(90deg, var(--ink-charcoal) 0 44%, var(--ink-black) 44% 100%);
  }
  .band--top { top: 0; }
  .band--bottom { bottom: 0; }

  .portrait-art {
    position: absolute;
    left: 18px;
    top: 14px;
    width: 262px;
    bottom: 14px;
    background: linear-gradient(100deg, var(--shadow-grey) 0 22%, var(--brand-blue) 22% 60%, var(--brand-blue-deep) 100%);
    border-top-right-radius: 80px;
  }

  .contact {
    position: absolute;
    left: 300px;
    right: 20px;
    top: 104px;
    color: var(--navy-text);
  }
  .contact__name {
    font-weight: 800;
    font-size: 17px;
    letter-spacing: 0.02em;
    text-transform: uppercase;
    text-align: center;
    width: 150px;
  }
  .contact__role {
    font-weight: 400;
    font-size: 11px;
    text-align: center;
    width: 150px;
    margin-top: 3px;
  }
  .contact__lines { margin-top: 26px; list-style: none; }
  .contact__line {
    display: flex;
    align-items: center;
    gap: 9px;
    font-size: 11px;
    font-weight: 500;
    margin-bottom: 6px;
  }
  .contact__icon { width: 12px; height: 12px; flex: none; }
</style>
</head>
<body>

  <section class="card card--front" aria-label="Business card front">
    <svg class="card__bands" viewBox="0 0 520 297" preserveAspectRatio="none" aria-hidden="true">
      <path d="M0 0 H520 V8 H0 Z" fill="var(--ink-black)"/>
      <path d="M0 8 H520 C430 10 360 22 300 38 C220 58 120 70 0 82 Z" fill="var(--ink-charcoal)"/>
      <path d="M0 8 H520 C430 14 360 24 300 36 C220 52 120 60 0 66 Z" fill="var(--brand-blue)"/>
      <path d="M0 297 H520 V289 H0 Z" fill="var(--ink-black)"/>
      <path d="M520 289 H0 C90 287 160 275 220 259 C300 239 400 227 520 215 Z" fill="var(--ink-charcoal)"/>
      <path d="M520 289 H0 C90 283 160 273 220 261 C300 245 400 237 520 231 Z" fill="var(--brand-blue)"/>
    </svg>
    <div class="brand">
      <span class="brand__dot"></span>
      <span class="brand__name">Bayfield Insurance Adjusters</span>
    </div>
  </section>

  <section class="card card--back" aria-label="Business card back">
    <div class="band band--top"></div>
    <div class="portrait-art" role="img" aria-label="Large blue wolf silhouette illustration with a grey offset shadow"></div>
    <div class="contact">
      <h1 class="contact__name">Daniel Ashcroft</h1>
      <p class="contact__role">Founder</p>
      <ul class="contact__lines">
        <li class="contact__line">
          <svg class="contact__icon" viewBox="0 0 12 12" aria-hidden="true">
            <rect x="3" y="0.8" width="6" height="10.4" rx="1" fill="none" stroke="currentColor" stroke-width="1"/>
            <line x1="5" y1="9.4" x2="7" y2="9.4" stroke="currentColor" stroke-width="0.9"/>
          </svg>
          555-204-7318
        </li>
        <li class="contact__line">
          <svg class="contact__icon" viewBox="0 0 12 12" aria-hidden="true">
            <rect x="0.7" y="2.5" width="10.6" height="7" fill="none" stroke="currentColor" stroke-width="0.9"/>
            <path d="M0.7 2.5 L6 6.6 L11.3 2.5" fill="none" stroke="currentColor" stroke-width="0.9"/>
          </svg>
          daniel@bayfieldclaims.com
        </li>
      </ul>
    </div>
    <div class="band band--bottom"></div>
  </section>

</body>
</html>
```